R. Talbin Group Business Card

We are looking for a business card mock-up.

Contact Information for Business Card

This is the information that needs to be included:
Name
Title
The R. Talbin Group Inc. Insurance Agents & Brokers (needs to be listed out in entirety)
Logo
License 0482316 (needs to be same sized font as phone number)
Address (728 North Vale Avenue, Los Angeles, CA 90047)
Telephone number ( 714-389-2076 ext. 131)Fax number (714-389-4152)
Email
Website (www.rtalbinagency.example)
Cities (Anaheim, Los Angeles, San Jose, Torrance)

```html
<!DOCTYPE html>
<html lang="en">
<head>
<meta charset="utf-8">
<title>R. Talbin Group Business Card</title>
<link href="https://fonts.googleapis.com/css2?family=Work+Sans:wght@400;500&family=Tinos&display=swap" rel="stylesheet">
<style>
  :root {
    --page-bg: #d9d4cd;
    --card-light: #e8e3dc;
    --card-dark: #2b2a29;
    --ring: #1e1d1c;
    --copper: #b5682f;
    --copper-text: #bf7440;
    --text-light: #e7e3dd;
    --text-soft: #c9c4bd;
  }
  * { margin: 0; padding: 0; box-sizing: border-box; }
  html, body { width: 1200px; height: 1047px; overflow: hidden; background: var(--page-bg); }
  .card {
    position: absolute; left: 100px; top: 251px; width: 1000px; height: 545px;
    border-radius: 22px; overflow: hidden; background: var(--card-light);
    box-shadow: 0 10px 30px rgba(0,0,0,0.18);
  }
  .card-art { position: absolute; inset: 0; }
  .card-info { position: absolute; left: 40px; top: 0; width: 560px; height: 100%; color: var(--text-light); font-family: "Work Sans", sans-serif; }
  .company-name { position: absolute; top: 34px; font-family: "Tinos", serif; font-size: 38px; letter-spacing: 0.5px; color: var(--text-soft); white-space: nowrap; }
  .company-tagline { position: absolute; top: 80px; font-family: "Tinos", serif; font-size: 12.5px; letter-spacing: 4.2px; color: var(--text-soft); white-space: nowrap; }
  .person-name { position: absolute; top: 131px; font-size: 33px; font-weight: 400; letter-spacing: 1.5px; color: var(--copper-text); }
  .detail { position: absolute; font-size: 21px; letter-spacing: 0.6px; white-space: nowrap; }
  .person-title { top: 183px; }
  .license { top: 225px; }
  .address-1 { top: 280px; }
  .address-2 { top: 313px; }
  .contact { display: flex; align-items: center; gap: 10px; }
  .contact svg { width: 14px; height: 14px; flex: none; }
  .phone { top: 386px; }
  .fax { top: 419px; }
  .email { top: 452px; }
  .web { top: 485px; }
  .web-highlight { color: var(--copper-text); }
  .brand-disc-content {
    position: absolute; left: 487px; top: 44px; width: 452px; height: 452px;
    border-radius: 50%;
    display: flex; flex-direction: column; align-items: center; justify-content: center;
    text-align: center; font-family: "Work Sans", sans-serif; color: var(--text-light);
  }
  .brand-mark { font-weight: 500; font-size: 48px; letter-spacing: 1px; line-height: 1.15; }
  .service-cities { margin-top: 26px; font-size: 17px; font-weight: 400; letter-spacing: 1px; line-height: 1.5; color: var(--text-light); }
</style>
</head>
<body>
  <div class="card">
    <svg class="card-art" width="1000" height="545" viewBox="0 0 1000 545" aria-hidden="true">
      <rect class="dark-panel" x="0" y="0" width="660" height="545" fill="var(--card-dark)"/>
      <circle class="light-halo" cx="713" cy="270" r="290" fill="var(--card-light)"/>
      <circle class="brand-ring" cx="713" cy="270" r="257" fill="none" stroke="var(--ring)" stroke-width="12"/>
      <circle class="brand-disc" cx="713" cy="270" r="226" fill="var(--copper)"/>
    </svg>

    <div class="brand-disc-content">
      <div class="brand-mark">R. Talbin<br>Group</div>
      <div class="service-cities">Anaheim · Los Angeles<br>San Jose · Torrance</div>
    </div>

    <div class="card-info">
      <div class="company-name">R. TALBIN GROUP INC.</div>
      <div class="company-tagline">INSURANCE AGENTS &amp; BROKERS</div>
      <div class="person-name">DANIEL WHITCOMB</div>
      <div class="detail person-title">Director</div>
      <div class="detail license">License 0482316</div>
      <div class="detail address-1">(728 North Vale Avenue,</div>
      <div class="detail address-2">Los Angeles, CA 90047)</div>
      <div class="detail contact phone">
        <svg viewBox="0 0 16 16"><path d="M3 1h3l1.5 4-2 1.2a9 9 0 0 0 4.3 4.3L11 8.5l4 1.5v3a2 2 0 0 1-2 2A13 13 0 0 1 1 3a2 2 0 0 1 2-2z" fill="var(--copper)"/></svg>
        <span>( 714-389-2076 ext. 131)</span>
      </div>
      <div class="detail contact fax">
        <svg viewBox="0 0 16 16"><rect x="4" y="1" width="8" height="4" fill="var(--copper)"/><rect x="1" y="6" width="14" height="6" rx="1.5" fill="var(--copper)"/><rect x="4" y="10" width="8" height="5" fill="var(--copper)"/></svg>
        <span>(714-389-4152)</span>
      </div>
      <div class="detail contact email">
        <svg viewBox="0 0 16 16"><rect x="1.5" y="3.5" width="13" height="9" fill="none" stroke="var(--copper)" stroke-width="1.5"/><path d="M1.5 3.5 8 9l6.5-5.5" fill="none" stroke="var(--copper)" stroke-width="1.5"/></svg>
        <span>info.rtalbinagency.example</span>
      </div>
      <div class="detail contact web">
        <svg viewBox="0 0 16 16"><circle cx="8" cy="8" r="6.5" fill="none" stroke="var(--copper)" stroke-width="1.5"/><path d="M1.5 8h13M8 1.5c-3 3.5-3 9.5 0 13M8 1.5c3 3.5 3 9.5 0 13" fill="none" stroke="var(--copper)" stroke-width="1.2"/></svg>
        <span><span class="web-highlight">www.rtalbinagency</span>.example</span>
      </div>
    </div>
  </div>
</body>
</html>
```